Design Business Cards

I need a new business card designed in two versions, one an International version and one a Japanese version.

Please ensure to submit designer files so we can edit it ourselves after the contest. We require the following file formats at minimum (AI, PSD, PNG).

I have attached 4 examples of letterpress business cards and the kind of style we want. Below you will find all the data for the front and back of the two cards, please come up with your own layout for how you think it should be best presented based on the data below, brief and examples.

I have also attached our company logo file.

Design Brief:

Simple and elegant business card, white, two sided. We will be producing two versions an international version and a Japanese version. We will require finished designs for both. These will be printed via letterpress and this should be considered when creating the design.

The (text) indicates what the information is and should not appear on the design. This is just for your reference.

International Front:

Company Logo

International Back:

Company Logo

Desmond Hartwick (Name)
Commercial Manager (Title)
+61 455 287 913 (Telephone)
randall@[login to view URL] (Email)

2078/4 Larkspur Rd
Melbourne, Vic, 3004
Australia
(Address)

United Kingdom | Australia | Hong Kong
(Worldwide Office Locations)

Japanese Front:

Company Logo

Desmond Hartwick (Name)
コマーシャルマネージャー (Title)

2078/4 Larkspur Rd
Melbourne, Vic, 3004
Australia
(Address)

イギリス|オーストラリア|香港

Japanese Back:

Company Logo

Desmond Hartwick (Name)

2078/4 Larkspur Rd
Melbourne, Vic, 3004
Australia
(Address)

```html
<!DOCTYPE html>
<html lang="en">
<head>
<meta charset="utf-8">
<title>Kestrel Events – Business Cards</title>
<link href="https://fonts.googleapis.com/css2?family=Lato:wght@400;700&family=Noto+Sans+JP:wght@400;700&display=swap" rel="stylesheet">
<style>
  :root {
    --backdrop: #4aa7ec;
    --card: #f4f4f2;
    --teal: #17857f;
    --ink: #2b2b2b;
    --muted: #4a4a4a;
  }
  html, body {
    margin: 0;
    padding: 0;
    width: 1200px;
    height: 895px;
    overflow: hidden;
    background: var(--backdrop);
    font-family: "Lato", "Noto Sans JP", sans-serif;
  }
  .sheet {
    position: relative;
    width: 1200px;
    height: 895px;
  }
  .card {
    position: absolute;
    width: 540px;
    height: 310px;
    background: var(--card);
    box-shadow: 0 6px 18px rgba(0, 0, 0, 0.18);
    overflow: hidden;
  }
  .card--intl-front { left: 40px;  top: 115px; }
  .card--intl-back  { left: 40px;  top: 470px; }
  .card--jp-front   { left: 620px; top: 115px; }
  .card--jp-back    { left: 620px; top: 470px; }

  .wordmark {
    position: absolute;
    margin: 0;
    color: var(--teal);
    font-family: "Lato", sans-serif;
    font-weight: 700;
    font-size: 34px;
    letter-spacing: 3px;
    text-transform: uppercase;
    white-space: nowrap;
  }
  .wordmark--centre {
    left: 0;
    right: 0;
    top: 105px;
    text-align: center;
  }
  .wordmark--side {
    left: 30px;
    top: 128px;
    font-size: 24px;
    letter-spacing: 2px;
  }

  .double-rule {
    position: absolute;
    height: 8px;
    border: 2px solid var(--teal);
  }
  .double-rule--top  { top: 28px;  left: 410px; width: 160px; }
  .double-rule--side { top: 200px; left: -20px; width: 120px; }

  .corner-address {
    position: absolute;
    right: 30px;
    bottom: 28px;
    margin: 0;
    font-size: 13px;
    color: var(--muted);
    text-align: right;
    white-space: nowrap;
  }
  .corner-address .details__name { margin-bottom: 6px; }

  .details {
    position: absolute;
    right: 30px;
    top: 40px;
    text-align: right;
    white-space: nowrap;
  }
  .details__name {
    margin: 0;
    font-size: 18px;
    font-weight: 400;
    color: var(--ink);
    text-transform: uppercase;
    letter-spacing: 0.5px;
  }
  .details__name .surname { color: var(--teal); }
  .details__title {
    margin: 2px 0 0;
    font-size: 14px;
    color: var(--teal);
  }
  .details__rule {
    width: 200px;
    height: 2px;
    margin: 8px 0 12px auto;
    background: var(--teal);
  }
  .details__line {
    margin: 0 0 4px;
    font-size: 13px;
    color: var(--muted);
  }
  .details__address {
    margin: 10px 0 0;
    font-size: 12px;
    line-height: 1.45;
    color: var(--muted);
  }

  .offices {
    position: absolute;
    left: 0;
    right: 0;
    bottom: 20px;
    margin: 0;
    text-align: center;
    font-size: 12px;
    letter-spacing: 1px;
    color: var(--teal);
  }
  [lang="ja"] { font-family: "Noto Sans JP", sans-serif; }
</style>
</head>
<body>
<main class="sheet">
  <section class="card card--intl-front" aria-label="International card front">
    <div class="double-rule double-rule--top"></div>
    <div class="double-rule double-rule--side"></div>
    <h1 class="wordmark wordmark--centre">Kestrel Events</h1>
    <p class="corner-address">2078/4 Larkspur Rd Melbourne, Vic 3004 Australia</p>
  </section>

  <section class="card card--intl-back" aria-label="International card back">
    <h2 class="wordmark wordmark--side">Kestrel Events</h2>
    <div class="details">
      <p class="details__name">Desmond <span class="surname">Hartwick</span></p>
      <p class="details__title">Commercial Manager</p>
      <div class="details__rule"></div>
      <p class="details__line">+61 455 287 913</p>
      <p class="details__line">desmond@kestrelevents.com</p>
      <p class="details__line">www.kestrelevents.com</p>
      <p class="details__address">2078/4 Larkspur Rd<br>Melbourne, Vic, 3004<br>Australia</p>
    </div>
    <p class="offices">United Kingdom | Australia | Hong Kong</p>
  </section>

  <section class="card card--jp-front" aria-label="Japanese card front">
    <h2 class="wordmark wordmark--side">Kestrel Events</h2>
    <div class="details">
      <p class="details__name">Desmond <span class="surname">Hartwick</span></p>
      <p class="details__title" lang="ja">コマーシャルマネージャー</p>
      <div class="details__rule"></div>
      <p class="details__address">2078/4 Larkspur Rd<br>Melbourne, Vic, 3004<br>Australia</p>
    </div>
    <p class="offices" lang="ja">イギリス | オーストラリア | 香港</p>
  </section>

  <section class="card card--jp-back" aria-label="Japanese card back">
    <div class="double-rule double-rule--top"></div>
    <div class="double-rule double-rule--side"></div>
    <h2 class="wordmark wordmark--centre">Kestrel Events</h2>
    <div class="corner-address">
      <p class="details__name">Desmond <span class="surname">Hartwick</span></p>
      <p class="details__address">2078/4 Larkspur Rd<br>Melbourne, Vic, 3004<br>Australia</p>
    </div>
  </section>
</main>
</body>
</html>
```